Letterhead design x 2, follower page, with compliments slip and envelope design X 2

Design letterhead x 2, follower page, with compliments slip and envelope x 2 for Harbor Venture Partners, a business broking company. Using the colours of the existing logo and a white background for a clean, sophisticated look.

Target Market(s)

Family Business owners and regular business owners looking to buy or sell their business, or improve the value of their business.

Font styles to use
Sans Serif

Requirements
Must have
• Letterhead design 1 - Additional logos for Crale Business Sales, NTQR and DWL to be included in a small size somewhere on the page. Crale Business Sales logo only to have the wording 'Powered By' alongside. Please do not distort the size of the logos.
Letterhead design 2 - Additional logos for NTQR and DWL to be included in a small size somewhere on the page. This design will not include the Crale Business Sales logo or the words 'Powered By'. Please do not distort the size of the logos.
Envelope design 1 - Please include an address window
Envelope design 2 - Do not include an address window

```html
<!DOCTYPE html>
<html lang="en">
<head>
<meta charset="utf-8">
<title>Harbor Venture Partners – Envelope</title>
<link rel="stylesheet" href="https://fonts.googleapis.com/css2?family=Outfit:wght@500&family=Noto+Sans:wght@400&display=swap">
<style>
  :root {
    --brand-orange: #f15a2b;
    --brand-grey: #9aa0a6;
    --paper: #ffffff;
    --ink: #1a1a1a;
  }
  html, body {
    margin: 0;
    padding: 0;
    width: 1200px;
    height: 600px;
    overflow: hidden;
    background: var(--paper);
  }
  .envelope {
    position: relative;
    width: 1200px;
    height: 600px;
    background: var(--paper);
    overflow: hidden;
  }
  .header-band {
    position: absolute;
    inset: 0 0 auto 0;
    width: 1200px;
    height: 160px;
  }
  .header-band .band-fill { fill: var(--brand-orange); }
  .header-band .band-rule {
    fill: none;
    stroke: var(--brand-grey);
    stroke-width: 4;
  }

  .brand {
    position: absolute;
    left: 125px;
    top: 180px;
    display: flex;
    align-items: center;
    gap: 26px;
  }
  .brand-mark {
    width: 108px;
    height: 108px;
    box-sizing: border-box;
    border: 5px solid var(--brand-grey);
    border-radius: 50%;
  }
  .brand-name {
    margin: 0;
    font-family: "Outfit", sans-serif;
    font-weight: 500;
    font-size: 34px;
    line-height: 34px;
    letter-spacing: -0.3px;
    color: var(--brand-orange);
  }
  .brand-name span { display: block; }

  .contact-bar {
    position: absolute;
    left: 0;
    right: 0;
    top: 536px;
    display: flex;
    justify-content: center;
    align-items: center;
    gap: 22px;
    font-family: "Noto Sans", sans-serif;
    font-size: 21px;
    color: var(--ink);
    margin: 0;
    padding: 0;
    list-style: none;
  }
  .contact-item {
    display: flex;
    align-items: center;
    gap: 10px;
  }
  .contact-icon {
    width: 24px;
    height: 24px;
    flex: none;
  }
  .contact-icon .icon-disc { fill: var(--brand-orange); }
  .contact-icon .icon-glyph { fill: var(--paper); }
</style>
</head>
<body>
<main class="envelope">
  <svg class="header-band" viewBox="0 0 1200 160" aria-hidden="true">
    <path class="band-fill" d="M0,0 H1200 V92 Q600,140 0,92 Z"/>
    <path class="band-rule" d="M0,110 Q600,158 1200,110"/>
  </svg>

  <header class="brand">
    <div class="brand-mark" aria-hidden="true"></div>
    <h1 class="brand-name"><span>Harbor</span><span>Venture</span><span>Partners</span></h1>
  </header>

  <ul class="contact-bar">
    <li class="contact-item">
      <svg class="contact-icon" viewBox="0 0 24 24" aria-hidden="true">
        <circle class="icon-disc" cx="12" cy="12" r="12"/>
        <path class="icon-glyph" d="M8.2,6.2 l2,2.3 c0.4,0.4 0.3,1 -0.1,1.4 l-0.8,0.8 c0.8,1.6 2.1,2.9 3.8,3.8 l0.8,-0.8 c0.4,-0.4 1,-0.4 1.4,-0.1 l2.3,2 c0.4,0.4 0.4,1 0,1.4 l-1,1 c-0.8,0.8 -2,0.9 -3,0.4 c-2.8,-1.4 -5,-3.6 -6.4,-6.4 c-0.5,-1 -0.4,-2.2 0.4,-3 l1,-1 c0.4,-0.4 1,-0.4 1.4,0 Z"/>
      </svg>
      <span>(1234) 555 20 118</span>
    </li>
    <li class="contact-item">
      <svg class="contact-icon" viewBox="0 0 24 24" aria-hidden="true">
        <circle class="icon-disc" cx="12" cy="12" r="12"/>
        <path class="icon-glyph" d="M6.5,8 h11 a0.8,0.8 0 0 1 0.8,0.8 v6.6 a0.8,0.8 0 0 1 -0.8,0.8 h-11 a0.8,0.8 0 0 1 -0.8,-0.8 v-6.6 a0.8,0.8 0 0 1 0.8,-0.8 Z M7,9.3 v0.5 l5,3.3 l5,-3.3 v-0.5 Z"/>
      </svg>
      <span>info@harborventure.com</span>
    </li>
    <li class="contact-item">
      <svg class="contact-icon" viewBox="0 0 24 24" aria-hidden="true">
        <circle class="icon-disc" cx="12" cy="12" r="12"/>
        <path class="icon-glyph" d="M12,5 a4.8,4.8 0 0 1 4.8,4.8 c0,3.4 -4.8,8.7 -4.8,8.7 s-4.8,-5.3 -4.8,-8.7 A4.8,4.8 0 0 1 12,5 Z M12,8 a1.8,1.8 0 1 0 0,3.6 a1.8,1.8 0 1 0 0,-3.6 Z"/>
      </svg>
      <span>street 45 harbor lane</span>
    </li>
  </ul>
</main>
</body>
</html>
```